Quiet Verses Across Winter Evenings

Need a BOOK COVER, SPINE, and BACK for above named book. This is the story of my late wife (a university professor) told through her own songs and poems. It is about the people she loved, especially her grand children, her extensive professional and life interests, her family, friends, and festivities, her illness, etc.
Updates

Need extra days to review

Target Market(s)

Family and friends

Font styles to use
Other font styles liked:
• Times New Roman

Requirements
Must have
• Regret I haven't given much thought to it...
Nice to have
• Regret I haven't given much thought to it..
Should not have

```html
<!DOCTYPE html>
<html lang="en">
<head>
<meta charset="utf-8">
<title>Quiet Verses Across Winter Evenings – Cover Concepts</title>
<link rel="stylesheet" href="https://fonts.googleapis.com/css2?family=Sansita+Swashed:wght@700&family=Roboto+Slab:wght@700;800&family=Roboto+Condensed:wght@700&family=Tinos:wght@700&family=Montserrat:wght@300;400&display=swap">
<style>
  :root {
    --bg-mint: #d4fbf4;
    --bg-warm: #fdf6dc;
    --gold-top: #fbc21a;
    --gold-deep: #f39a00;
    --ink: #0c0a08;
    --text: #2a2a2a;
    --plum: #6a1fa0;
    --plum-deep: #4b1478;
    --white: #ffffff;
    --sky-teal: #7fd6cf;
    --sky-cloud: #e9efe6;
    --amber: #d9a35a;
    --bronze: #a8742c;
    --brick: #b3261e;
    --spine-teal: #6fa9a3;
  }
  * { box-sizing: border-box; margin: 0; padding: 0; }
  html, body { width: 1200px; height: 1000px; overflow: hidden; }
  body {
    position: relative;
    background: radial-gradient(ellipse 45% 50% at 50% 52%, var(--bg-warm) 0%, var(--bg-mint) 100%);
  }

  /* Book row */
  .books {
    position: absolute; top: 40px; left: 0; right: 0;
    display: flex; justify-content: center; gap: 44px;
  }
  .book { display: flex; height: 420px; box-shadow: 0 14px 30px rgba(0,0,0,.22); }
  .spine {
    width: 30px;
    display: flex; align-items: center; justify-content: space-between;
    padding: 16px 0;
    writing-mode: vertical-rl;
  }
  .cover { width: 280px; position: relative; overflow: hidden; }

  /* Warm edition */
  .book--warm .spine { background: linear-gradient(var(--gold-top), var(--gold-deep)); border-right: 1px solid rgba(0,0,0,.15); }
  .book--warm .spine-title { font-family: "Sansita Swashed", cursive; color: var(--plum); font-size: 13px; }
  .book--warm .spine-author { font-family: "Roboto Slab", serif; color: var(--plum-deep); font-size: 11px; font-weight: 800; }
  .book--warm .cover { background: linear-gradient(180deg, var(--gold-top) 0%, var(--gold-deep) 74%, var(--ink) 92%); }
  .note-field {
    position: absolute; inset: 0 0 90px 0;
    background:
      radial-gradient(circle at 20% 15%, rgba(255,240,190,.45) 0 6%, transparent 14%),
      radial-gradient(circle at 80% 30%, rgba(255,240,190,.4) 0 5%, transparent 12%),
      radial-gradient(circle at 15% 55%, rgba(255,240,190,.35) 0 5%, transparent 12%),
      radial-gradient(circle at 85% 65%, rgba(255,240,190,.35) 0 5%, transparent 12%);
  }
  .warm-title {
    position: absolute; top: 52px; left: 0; right: 0; text-align: center;
    font-family: "Sansita Swashed", cursive; color: var(--plum);
  }
  .warm-title .line-main { display: block; font-size: 38px; line-height: 1; }
  .warm-title .line-sub { display: block; font-size: 19px; color: var(--plum-deep); margin-top: 6px; }
  .warm-tree {
    position: absolute; left: 30px; right: 30px; top: 170px; height: 180px;
    border-radius: 50% 50% 10px 10px / 60% 60% 10px 10px;
    background: radial-gradient(ellipse at 50% 40%, #3a1a4a 0%, #6a1fa0 40%, rgba(40,20,10,.6) 75%, transparent 100%);
  }
  .warm-author {
    position: absolute; bottom: 24px; left: 0; right: 0; text-align: center;
    font-family: "Roboto Slab", serif; font-weight: 800; color: var(--white); font-size: 16px;
  }

  /* Sky edition */
  .book--sky .spine { background: linear-gradient(var(--spine-teal), var(--sky-cloud) 45%, var(--bronze) 80%, var(--ink)); }
  .book--sky .spine-title,
  .book--sky .spine-author { font-family: "Roboto Slab", serif; color: var(--ink); font-size: 10px; font-weight: 700; }
  .book--sky .cover { background: linear-gradient(180deg, var(--sky-teal) 0%, var(--sky-cloud) 28%, var(--amber) 60%, var(--bronze) 78%, var(--ink) 96%); }
  .cloud-field {
    position: absolute; inset: 0 0 100px 0;
    background:
      radial-gradient(ellipse 40% 14% at 25% 12%, rgba(255,255,255,.7), transparent),
      radial-gradient(ellipse 35% 12% at 80% 38%, rgba(255,255,255,.55), transparent),
      radial-gradient(ellipse 30% 10% at 20% 50%, rgba(255,255,255,.4), transparent),
      radial-gradient(ellipse 25% 10% at 90% 62%, rgba(255,255,255,.45), transparent);
  }
  .sky-title {
    position: absolute; top: 52px; left: 0; right: 0; text-align: center;
    font-family: "Roboto Slab", serif; font-weight: 800; color: var(--brick);
  }
  .sky-title .line-main { display: block; font-size: 24px; }
  .sky-title .line-join {
    display: inline-flex; align-items: center; justify-content: center;
    width: 30px; height: 30px; border-radius: 50%; margin: 8px 0;
    background: var(--brick); color: var(--white); font-size: 8px;
  }
  .sky-title .line-sub { display: block; font-size: 24px; }
  .sky-tree {
    position: absolute; left: 35px; right: 35px; top: 180px; height: 170px;
    border-radius: 50% 50% 10px 10px / 60% 60% 10px 10px;
    background: radial-gradient(ellipse at 50% 40%, #7a3a14 0%, #b3561e 40%, rgba(40,20,10,.55) 75%, transparent 100%);
  }
  .sky-author {
    position: absolute; bottom: 28px; left: 0; right: 0; text-align: center;
    font-family: "Roboto Condensed", sans-serif; font-weight: 700; color: var(--white); font-size: 14px;
  }

  /* Concept panel */
  .concept {
    position: absolute; top: 472px; left: 0; right: 0;
    text-align: center; color: var(--text);
    font-family: "Montserrat", sans-serif; font-weight: 300;
    font-size: 22.5px; line-height: 28px;
  }
  .concept-title {
    font-family: "Tinos", "Times New Roman", serif; font-weight: 700;
    font-size: 43px; line-height: 56px; color: var(--ink);
  }
  .concept-intro { font-weight: 400; }
  .concept p { max-width: 900px; margin: 0 auto 27px; }
  .concept .concept-intro { margin-bottom: 27px; }
  .concept strong { font-weight: 400; }
</style>
</head>
<body>
  <section class="books">
    <article class="book book--warm">
      <div class="spine">
        <span class="spine-title">Quiet Verses Across Winter Evenings</span>
        <span class="spine-author">Meera Anand Kulkarni</span>
      </div>
      <div class="cover">
        <div class="note-field" role="img" aria-label="Scattered light music notes across the gold background"></div>
        <h1 class="warm-title">
          <span class="line-main">Quiet Verses</span>
          <span class="line-sub">Across Winter Evenings</span>
        </h1>
        <div class="warm-tree" role="img" aria-label="Illustration of a family tree with dark branches and purple and black leaves"></div>
        <p class="warm-author">Meera Anand Kulkarni</p>
      </div>
    </article>

    <article class="book book--sky">
      <div class="spine">
        <span class="spine-title">Quiet Verses Across Winter Evenings</span>
        <span class="spine-author">Meera Anand Kulkarni</span>
      </div>
      <div class="cover">
        <div class="cloud-field" role="img" aria-label="Soft white clouds and faint music notes in a teal to amber sky"></div>
        <h1 class="sky-title">
          <span class="line-main">Quiet Verses</span>
          <span class="line-join">Across</span>
          <span class="line-sub">Winter Evenings</span>
        </h1>
        <div class="sky-tree" role="img" aria-label="Illustration of a family tree with autumn red and amber leaves"></div>
        <p class="sky-author">Meera Anand Kulkarni</p>
      </div>
    </article>
  </section>

  <section class="concept">
    <h2 class="concept-title">– Concept –</h2>
    <p class="concept-intro">At first we’re sorry for your loss!</p>
    <p>There are some elements that are meant to suit the contest brief :</p>
    <p><strong>-The tree</strong>, especially the roots and the trunk are related to our grand parents and in this case they’re related to your late wife. wherase the leaves and branches are related to their sons and their grand children and the relations you menthioned in the brief. There ia a gradient from darker to lighter to be like ages.</p>
    <p><strong>-The clouds</strong> to show that is the sky and the feelings of sprity.</p>
    <p><strong>-Music elements</strong> to show that the book would radiate words of love and happiness although the tree roots are black. This is the end and I hope you like my project!</p>
  </section>
</body>
</html>
```